Real Estate Investing company needs a business card design

We need a business card design for new Real Estate Investment Company called "Brightgate Holdings, LLC." We buy homes for cash and close quickly in any situation. Our company provides an easy and fast option for home owners who are in tough situations who need to sell their home fast and don't want realtor fees or other listing hassles. We also renovate and resell our homes which helps provide housing for the community. We would like to see designs that use the colors blue and white to match our company logo or other colors that may match our company logo. The final design should communicate trust and easy process.
Industry/Entity Type
Business
Contact Information for Business Card
Front should have company name and company logo. back of card should have company logo and area to list services.
Look and feel

```html
<!DOCTYPE html>
<html lang="en">
<head>
<meta charset="UTF-8">
<title>Brightgate Holdings – Business Card</title>
<link rel="stylesheet" href="https://fonts.googleapis.com/css2?family=Open+Sans:wght@400;700;800&family=Montserrat:wght@400&display=swap">
<style>
  :root {
    --page: #e9eaec;
    --card: #ffffff;
    --card-edge: #cfd2d6;
    --brand-blue: #1b4c97;
    --text-grey: #6a6d72;
    --band-grey: #d6d7d9;
    --band-light: #eeeff0;
  }
  * { margin: 0; padding: 0; box-sizing: border-box; }
  html, body {
    width: 1200px; height: 970px; overflow: hidden;
    background: var(--page);
  }
  .card {
    position: absolute; left: 80px; top: 195px;
    width: 1040px; height: 580px;
    background: var(--card);
    border: 1px solid var(--card-edge);
    overflow: hidden;
    font-family: "Montserrat", Arial, sans-serif;
    color: var(--text-grey);
  }
  .brand {
    position: absolute; left: 50px; top: 60px;
    display: flex; align-items: center; gap: 18px;
  }
  .brand-square { width: 34px; height: 34px; background: var(--brand-blue); }
  .brand-name {
    font-family: "Open Sans", Arial, sans-serif;
    font-weight: 800; font-size: 50px; line-height: 1.02;
    color: var(--brand-blue); letter-spacing: 0.5px;
  }
  .person { position: absolute; left: 50px; top: 300px; }
  .person-name {
    font-family: "Open Sans", Arial, sans-serif;
    font-weight: 700; font-size: 31px; color: var(--brand-blue);
    letter-spacing: 0.5px; line-height: 1.2;
  }
  .person-title { font-size: 22px; margin-top: 6px; }
  .contacts {
    position: absolute; left: 50px; top: 402px;
    list-style: none; font-size: 23px; line-height: 34px;
  }
  .contacts li { display: flex; align-items: center; gap: 14px; }
  .contacts svg { width: 22px; height: 22px; fill: var(--brand-blue); flex: none; }
  .services { position: absolute; left: 638px; top: 255px; }
  .services-heading {
    font-family: "Open Sans", Arial, sans-serif;
    font-weight: 700; font-size: 28px; color: var(--brand-blue);
    margin-bottom: 6px;
  }
  .services-list { list-style: none; font-size: 22px; line-height: 32.3px; }
  .services-list li { display: flex; align-items: center; gap: 12px; }
  .services-list svg { width: 22px; height: 20px; flex: none; }
  .footer-band {
    position: absolute; left: 0; bottom: 0;
    width: 1040px; height: 56px;
    background: linear-gradient(90deg, var(--card) 0%, var(--band-light) 35%, var(--band-grey) 60%, var(--band-grey) 100%);
  }
  .website {
    position: absolute; left: 609px; top: 537px;
    font-family: "Open Sans", Arial, sans-serif;
    font-size: 23px; color: var(--brand-blue);
  }
</style>
</head>
<body>
  <div class="card">
    <div class="brand">
      <div class="brand-square"></div>
      <div class="brand-name">BRIGHTGATE<br>HOLDINGS</div>
    </div>

    <div class="person">
      <div class="person-name">DANIEL REYES</div>
      <div class="person-title">Chief Executive Officer</div>
    </div>

    <ul class="contacts">
      <li>
        <svg viewBox="0 0 24 24"><path d="M8 2h8a1.5 1.5 0 0 1 1.5 1.5v17A1.5 1.5 0 0 1 16 22H8a1.5 1.5 0 0 1-1.5-1.5v-17A1.5 1.5 0 0 1 8 2zm1 3v8h6V5zm1 10v2h4v-2z"/></svg>
        <span>+ 000 000 0000</span>
      </li>
      <li>
        <svg viewBox="0 0 24 24"><path d="M7 3h10v5H7zM3 9h18a1 1 0 0 1 1 1v7h-4v4H6v-4H2v-7a1 1 0 0 1 1-1zm5 7v3h8v-3z"/></svg>
        <span>+ 000 000 0000</span>
      </li>
      <li>
        <svg viewBox="0 0 24 24"><path d="M2 5h20v14H2zm2 2v.5l8 5.5 8-5.5V7l-8 5.5z"/></svg>
        <span>info@brightgateholdings.com</span>
      </li>
    </ul>

    <div class="services">
      <div class="services-heading">SERVICES</div>
      <ul class="services-list">
        <li><svg viewBox="0 0 22 20"><path d="M2 11l6 6L20 3" fill="none" stroke="#1b4c97" stroke-width="3"/></svg>Lead Generation</li>
        <li><svg viewBox="0 0 22 20"><path d="M2 11l6 6L20 3" fill="none" stroke="#1b4c97" stroke-width="3"/></svg>Customer Acquisition</li>
        <li><svg viewBox="0 0 22 20"><path d="M2 11l6 6L20 3" fill="none" stroke="#1b4c97" stroke-width="3"/></svg>Internet Marketing</li>
        <li><svg viewBox="0 0 22 20"><path d="M2 11l6 6L20 3" fill="none" stroke="#1b4c97" stroke-width="3"/></svg>Phone Verified Leads</li>
        <li><svg viewBox="0 0 22 20"><path d="M2 11l6 6L20 3" fill="none" stroke="#1b4c97" stroke-width="3"/></svg>Performance Analytics</li>
        <li><svg viewBox="0 0 22 20"><path d="M2 11l6 6L20 3" fill="none" stroke="#1b4c97" stroke-width="3"/></svg>Inbound Services</li>
      </ul>
    </div>

    <div class="footer-band" role="img" aria-label="Decorative footer band in blue and grey tones"></div>

    <div class="website">www.brightgateholdings.com</div>
  </div>
</body>
</html>
```